Willow Frost: CBD and Herbal Topical Pain product needs a brochure

We need a brochure that educates customers on the product. The product combines traditional Chinese herbs used for pain and swelling with a strong dose of CBD to apply topical with a glass, roll-on applicator. We would like to see dark blue as a dominant color or anything ice related. The logo is an iceberg but doesn't need to be included.

Target Market(s)

Cannabis Dispensaries, Chiro, Acu offices,
Health / Wellness, Alternative Medicine

Industry/Entity Type

Alternative Medicine

Colors
0455a3

Requirements
Must have
• Willow Frost
• 500mg CBD in 1oz
• For: Muscle, Joint Pain, Swelling, Acute Injuries, Chronic Pain, Arthritis
• Directions: Apply a thin layer of herbal formula over the affected area. Apply as needed.
• Caution: Avoid hot water shortly after application.
• Ingredients: Angelica Root, Camphor, Cannabidoil (CBD), Cinnamon, Dandelion, Gardenia, Ginger, Licorice, Menthol, Myrrh, Phellodendron Bark, Rhubarb, Safflower, Sesame Oil, Scutellaria
• Highlight amount of CBD: 500mg
• Secondary highlights it includes Turmeric and Magnesium
• Easy Roll-On Topical Pain Relief for Muscle Spasms, Joint Pain, Strains, Sprains, Swelling
• Increases circulation to increase recovery time. Great for athletes
• Stops pain by numbing painful, slower deep nerve signals by stimulating the faster, superficial nerves with a cooling sensation
• Reduce painful swelling and heat involved with inflammation.
• Breaks up damaged tissue to enhance the natural healing process
• Ingredients
• Dang Gui – Angelica : reduces swelling, generates tissue, alleviates pain, expels pus
• Cinnamon –Gui Zhi decreases arthritic pain
• Carthamus Flower / safflower –Hong Hua - reduces swelling, alleviates pain,
• Rhubarb – Da Huang -bruising, acute and chronic swelling
• Licorice –Gan Cao - alleviates spasms, anti-inflammatory
• Phellodendron Huang Bai– reduces swelling and pain
• Dandelion – Pu Gong Ying – reduces swelling and nodules, anti-inflammatory
• Mo Yao – Myrrh – reduces swelling, pain, bruising, and masses, promotes healing
• Ginger – Gan Jiang – chronic swelling, increases circulation
• Gardenia – Zhi Zi- Reduces swelling from trauma, bruising
• Scutellaria – Huang Qin – hot sores, swelling,
• Magnesium – helps muscle spasms
• Camphor – mild, local anesthetic effect, alleviates pain, pain and swelling from sprains
• Menthol – rashes, swelling, relaxes muscles
• Turmeric – reduces inflammation and swelling
• Sesame Oil – carrier oil
• Cannabidiol (CBD) Isolate
• Colloidal Silver (Natural Preservative)
• Formulated by a Herbalist and Doctor of Chinese Medicine, Dr. Dennis Harlow, DAOM
Nice to have
• Iceberg or ice theme
• Copy:
• Willow Frost blends traditional Chinese herbs with a potent dose of hemp derived cannabidiol (CBD) isolate. Instantly feel the cooling icy sensation penetrate deep into sore muscles and joints to sooth away pain.
• Not only does the menthol give a temporary cooling effect which helps numb pain, the other herbal ingredients continue to soothe tight, achy muscles and joints. It can also be applied for an acute sprain or strain to reduce swelling, just like applying ice.
• Ice is used by athletes and recommended by doctors to reduce pain and swelling. Willow Frost can reduce pain and swelling without having to carry a bag of ice around.
• With the easy roll-on application, you dont even have to get your hands cold!
• Traditional Chinese Medicine has used the same herbs for thousands of years to help ease the pain of injuries during battle. Herbal plasters, liniments, and oils were the most common application to maximize the healing benefits of the herbs. Willow Frost uses organic, raw herbs which are ground into a fine powder and further extracted in sesame oil. Once extracted, the oil is filtered and then CBD is then added as the oil is cooling.
• Pictures of a few of the herbs - I have a few already if needed

```html
<!DOCTYPE html>
<html lang="en">
<head>
<meta charset="utf-8">
<title>Willow Frost Brochure</title>
<link rel="stylesheet" href="https://fonts.googleapis.com/css2?family=Lato:ital,wght@0,400;0,700;0,900;1,400&display=swap">
<style>
  :root {
    --brand-blue: #0455a3;
    --navy: #26233f;
    --paper: #ffffff;
    --paper-shade: #f1f2f4;
    --ink: #3d3f45;
    --backdrop: #d6d7d9;
  }
  * { box-sizing: border-box; margin: 0; padding: 0; }
  html, body { width: 1200px; height: 1200px; overflow: hidden; }
  body {
    background: var(--backdrop);
    font-family: "Lato", sans-serif;
    color: var(--ink);
    position: relative;
  }
  .spread {
    position: absolute;
    left: 40px;
    width: 1120px;
    height: 540px;
    display: grid;
    grid-template-columns: repeat(3, 1fr);
    box-shadow: 0 8px 24px rgba(0,0,0,.18);
  }
  .spread--inside { top: 40px; }
  .spread--outside { top: 620px; }
  .panel { position: relative; overflow: hidden; background: var(--paper); }
  .panel--blue { background: var(--brand-blue); color: #fff; }
  .panel + .panel { border-left: 1px solid rgba(0,0,0,.06); }

  ul.bullets { list-style: none; }
  ul.bullets li { position: relative; padding-left: 16px; margin-bottom: 9px; font-size: 11.5px; line-height: 1.35; }
  ul.bullets li::before {
    content: ""; position: absolute; left: 0; top: 4px;
    width: 7px; height: 7px; border-radius: 50%; background: var(--brand-blue);
  }

  /* inside: panel 1 */
  .intro { padding: 34px 28px 0 30px; }
  .intro__title { color: var(--brand-blue); font-weight: 900; font-size: 38px; line-height: 1; }
  .intro__dose { font-weight: 700; font-size: 18px; color: #222; margin: 8px 0 14px; }
  .photo { position: absolute; }
  .photo--citrus-drinks {
    left: 0; right: 0; bottom: 0; height: 190px;
    background: linear-gradient(160deg, #fbfbfb 0%, #f6d9a8 35%, #f0a94c 65%, #e9eef0 100%);
  }

  /* inside: panel 2 */
  .photo--berry-drinks {
    left: 0; right: 0; top: 0; height: 250px;
    background: radial-gradient(ellipse at 55% 55%, #d8364d 0%, #c9394f 30%, #f0c24e 55%, #e8efe6 80%);
  }
  .highlights { position: absolute; left: 22px; right: 22px; top: 268px; }
  .highlights__title { font-weight: 900; font-size: 19px; color: #222; margin-bottom: 12px; }
  .highlights__title span { color: var(--brand-blue); }
  .highlights ul.bullets li { font-size: 11px; margin-bottom: 7px; }

  /* inside: panel 3 */
  .herb-list { list-style: none; padding: 24px 22px 0 24px; }
  .herb-list li { font-size: 10.4px; line-height: 1.3; margin-bottom: 3px; }
  .herb-list b { font-weight: 900; }
  .herb-list .credit { margin-top: 4px; }
  .panel__footer {
    position: absolute; left: 24px; right: 22px; bottom: 24px;
    border-top: 1px solid rgba(255,255,255,.6); padding-top: 12px;
    font-size: 22px; font-weight: 400; letter-spacing: .5px;
  }

  /* outside: panel 1 */
  .photo--sunset-drink {
    left: 0; right: 0; top: 0; height: 150px;
    background: linear-gradient(180deg, #3a6fb0 0%, #9fbde0 35%, #f5b08e 65%, #ffffff 100%);
  }
  .story { position: absolute; left: 26px; right: 24px; top: 150px; }
  .story ul.bullets li { font-size: 10.6px; font-style: italic; margin-bottom: 8px; line-height: 1.3; }

  /* outside: panel 2 */
  .label {
    background: var(--navy); color: #fff; text-align: center;
  }
  .label__name { font-weight: 900; font-size: 15px; }
  .label__sub { font-weight: 700; }
  .label__line { font-size: 8px; opacity: .9; }
  .label--small { width: 118px; margin: 58px auto 0; padding: 16px 8px 10px; }
  .label--small .label__sub { font-size: 11px; margin-top: 26px; }
  .contact {
    position: absolute; left: 0; right: 0; bottom: 56px; text-align: center;
    font-size: 13.5px; line-height: 1.45;
  }

  /* outside: panel 3 */
  .photo--iced-coffee {
    left: 0; right: 0; top: 0; height: 300px;
    background: radial-gradient(ellipse at 58% 55%, #7a3c14 0%, #b0703a 22%, #d9c2a7 42%, #eceeef 70%, #f7f7f7 100%);
  }
  .cover-frame {
    position: absolute; left: 64px; right: 64px; top: 318px; height: 200px;
    border: 2px dotted #8a8c93; padding: 12px;
  }
  .label--cover { height: 100%; padding: 22px 12px 0; }
  .label--cover .label__name { font-size: 26px; }
  .label--cover .label__sub { font-size: 17px; margin-top: 46px; }
  .label--cover .label__line { font-size: 10px; margin-top: 4px; }
</style>
</head>
<body>

<section class="spread spread--inside">
  <div class="panel">
    <div class="intro">
      <h1 class="intro__title">Willow Frost</h1>
      <p class="intro__dose">500mg CBD in 1oz</p>
      <ul class="bullets">
        <li>For: Muscle, Joint Pain, Swelling, Acute Injuries, Chronic Pain, Arthritis</li>
        <li>Directions: Apply a thin layer of herbal formula over the affected area. Apply as needed.</li>
        <li>Caution: Avoid hot water shortly after application.</li>
        <li>Ingredients: Angelica Root, Camphor, Cannabidoil (CBD), Cinnamon, Dandelion, Gardenia, Ginger, Licorice, Menthol, Myrrh, Phellodendron Bark, Rhubarb, Safflower, Sesame Oil, Scutellaria</li>
      </ul>
    </div>
    <div class="photo photo--citrus-drinks" role="img" aria-label="Photo of two glasses of iced citrus drink with berries"></div>
  </div>

  <div class="panel">
    <div class="photo photo--berry-drinks" role="img" aria-label="Photo of red berry drinks garnished with mint and marigold flowers"></div>
    <div class="highlights">
      <h2 class="highlights__title">Highlight amount of CBD: <span>500mg</span></h2>
      <ul class="bullets">
        <li>Secondary highlights it includes Turmeric and Magnesium</li>
        <li>Easy Roll-On Topical Pain Relief for Muscle Spasms, Joint Pain, Strains, Sprains, Swelling</li>
        <li>Increases circulation to increase recovery time. Great for athletes</li>
        <li>Stops pain by numbing painful, slower deep nerve signals by stimulating the faster, superficial nerves with a cooling sensation</li>
        <li>Reduce painful swelling and heat involved with inflammation.</li>
        <li>Breaks up damaged tissue to enhance the natural healing process</li>
        <li>Ingredients</li>
      </ul>
    </div>
  </div>

  <div class="panel panel--blue">
    <ul class="herb-list">
      <li><b>Dang Gui</b> – Angelica : reduces swelling, generates tissue, alleviates pain, expels pus</li>
      <li><b>Cinnamon</b> – Gui Zhi decreases arthritic pain</li>
      <li><b>Carthamus Flower / safflower</b> – Hong Hua - reduces swelling, alleviates pain</li>
      <li><b>Rhubarb</b> – Da Huang - bruising, acute and chronic swelling</li>
      <li><b>Licorice</b> – Gan Cao - alleviates spasms, anti-inflammatory</li>
      <li><b>Phellodendron Huang Bai</b> – reduces swelling and pain</li>
      <li><b>Dandelion</b> – Pu Gong Ying – reduces swelling and nodules, anti-inflammatory</li>
      <li><b>Mo Yao</b> – Myrrh – reduces swelling, pain, bruising, and masses, promotes healing</li>
      <li><b>Ginger</b> – Gan Jiang – chronic swelling, increases circulation</li>
      <li><b>Gardenia</b> – Zhi Zi - Reduces swelling from trauma, bruising</li>
      <li><b>Scutellaria</b> – Huang Qin – hot sores, swelling</li>
      <li><b>Magnesium</b> – helps muscle spasms</li>
      <li><b>Camphor</b> – mild, local anesthetic effect, alleviates pain, pain and swelling from sprains</li>
      <li><b>Menthol</b> – rashes, swelling, relaxes muscles</li>
      <li><b>Turmeric</b> – reduces inflammation and swelling</li>
      <li><b>Sesame Oil</b> – carrier oil</li>
      <li>Cannabidiol (CBD) Isolate</li>
      <li>Colloidal Silver (Natural Preservative)</li>
      <li class="credit">Formulated by a Herbalist and Doctor of Chinese Medicine, Dr. Dennis Harlow, DAOM</li>
    </ul>
    <p class="panel__footer">Alternative Medicine</p>
  </div>
</section>

<section class="spread spread--outside">
  <div class="panel">
    <div class="photo photo--sunset-drink" role="img" aria-label="Photo of a peach iced drink with a straw against a blue sky"></div>
    <div class="story">
      <ul class="bullets">
        <li>Willow Frost blends traditional Chinese herbs with a potent dose of hemp derived cannabidiol (CBD) isolate. Instantly feel the cooling icy sensation penetrate deep into sore muscles and joints to sooth away pain.</li>
        <li>Not only does the menthol give a temporary cooling effect which helps numb pain, the other herbal ingredients continue to soothe tight, achy muscles and joints. It can also be applied for an acute sprain or strain to reduce swelling, just like applying ice.</li>
        <li>Ice is used by athletes and recommended by doctors to reduce pain and swelling. Willow Frost can reduce pain and swelling without having to carry a bag of ice around.</li>
        <li>With the easy roll-on application, you dont even have to get your hands cold!</li>
        <li>Traditional Chinese Medicine has used the same herbs for thousands of years to help ease the pain of injuries during battle. Herbal plasters, liniments, and oils were the most common application to maximize the healing benefits of the herbs. Willow Frost uses organic, raw herbs which are ground into a fine powder</li>
      </ul>
    </div>
  </div>

  <div class="panel panel--blue">
    <div class="label label--small">
      <p class="label__name">Willow Frost</p>
      <p class="label__sub">Pain Relief</p>
      <p class="label__line">Menthol, CBD, Turmeric &amp; Magnesium</p>
      <p class="label__line">1 fl oz</p>
    </div>
    <address class="contact" style="font-style: normal;">
      Address: 12 Glacier Lane, Portland<br>
      Phone: 555 0142<br>
      Email: hello@willowfrost-care.com<br>
      www.willowfrost-care.com
    </address>
  </div>

  <div class="panel">
    <div class="photo photo--iced-coffee" role="img" aria-label="Photo of a tall glass of iced coffee with cream swirling"></div>
    <div class="cover-frame">
      <div class="label label--cover">
        <p class="label__name">Willow Frost</p>
        <p class="label__sub">Pain Relief</p>
        <p class="label__line">Menthol, CBD, Turmeric &amp; Magnesium</p>
        <p class="label__line">1 fl oz</p>
      </div>
    </div>
  </div>
</section>

</body>
</html>
```